Business Cards for Internet Security Company

Awesome designers! This is the opportunity to help design cards for a forward thinking network security company. They use threat information gathered from peer groups to make intelligent decisions on what threats are relevant and which arent. ( not that you need this to do designs, but just so you know where they are coming from. ) :-)

We'd like to see a two side design and the deliverables will be in illustrator 4. The logo is attached and the logo colors are attached in the JPG and I've attached a an eps of the logo and icon

Security

```html
<!DOCTYPE html>
<html lang="en">
<head>
<meta charset="utf-8">
<title>Kelnara Business Cards</title>
<link rel="stylesheet" href="https://fonts.googleapis.com/css2?family=Roboto+Condensed:ital,wght@0,400;0,700;1,400&display=swap">
<style>
  :root {
    --page-bg: #ececec;
    --card-bg: #f7f8f9;
    --navy: #2d5573;
    --steel-blue: #4b79b1;
    --ink: #3f5f7b;
    --ink-soft: #5a7fa8;
    --shadow: rgba(0, 0, 0, 0.12);
  }
  * { box-sizing: border-box; margin: 0; padding: 0; }
  html, body {
    width: 1200px;
    height: 1001px;
    overflow: hidden;
    background: var(--page-bg);
    font-family: "Roboto Condensed", "Arial Narrow", sans-serif;
  }
  .sheet {
    position: relative;
    width: 1200px;
    height: 1001px;
    display: flex;
    align-items: center;
    justify-content: center;
    gap: 60px;
  }
  .card {
    position: relative;
    width: 525px;
    height: 300px;
    background: var(--card-bg);
    box-shadow: 0 6px 18px var(--shadow);
    overflow: hidden;
  }
  .brand {
    display: flex;
    align-items: center;
    gap: 12px;
    color: var(--navy);
    font-weight: 400;
  }
  .brand-dot {
    border-radius: 50%;
    background: var(--steel-blue);
    flex: none;
  }
  .band {
    position: absolute;
    left: 0;
    right: 0;
    height: 9px;
    display: flex;
    gap: 6px;
  }
  .band-light { background: var(--steel-blue); }
  .band-dark { background: var(--navy); flex: 1; }

  /* Front side */
  .card-front .brand {
    position: absolute;
    left: 70px;
    top: 92px;
    font-size: 74px;
    letter-spacing: 1px;
  }
  .card-front .brand-dot { width: 40px; height: 40px; }
  .card-front .band { bottom: 42px; flex-direction: row; }
  .card-front .band-dark { flex: 1; }
  .card-front .band-light { width: 150px; }

  /* Back side */
  .card-back .brand {
    position: absolute;
    left: 24px;
    top: 22px;
    font-size: 58px;
    letter-spacing: 1px;
  }
  .card-back .brand-dot { width: 30px; height: 30px; }
  .card-back .band { top: 148px; }
  .card-back .band-light { width: 130px; }
  .holder {
    position: absolute;
    left: 26px;
    top: 104px;
    color: var(--ink);
  }
  .holder-name { font-size: 16px; font-weight: 700; }
  .holder-role {
    position: absolute;
    left: 26px;
    top: 166px;
    font-size: 13px;
    font-style: italic;
    color: var(--ink-soft);
    line-height: 1.35;
  }
  .contact {
    position: absolute;
    left: 250px;
    top: 176px;
    list-style: none;
    color: var(--ink);
    font-size: 14px;
    font-weight: 700;
    line-height: 1.3;
  }
  .contact li {
    display: flex;
    align-items: flex-start;
    gap: 10px;
    margin-bottom: 4px;
  }
  .contact svg { flex: none; width: 14px; height: 14px; margin-top: 2px; fill: var(--navy); }
</style>
</head>
<body>
<main class="sheet">

  <section class="card card-back" aria-label="Card back">
    <div class="brand"><span class="brand-dot"></span><span class="brand-name">Kelnara</span></div>
    <p class="holder"><span class="holder-name">Mara Tolsen</span></p>
    <div class="band"><span class="band-light"></span><span class="band-dark"></span></div>
    <p class="holder-role">Chief Executive<br>Officer &amp; Co-Founder</p>
    <ul class="contact">
      <li>
        <svg viewBox="0 0 14 14"><path d="M7 0a4.5 4.5 0 0 0-4.5 4.5C2.5 8 7 14 7 14s4.5-6 4.5-9.5A4.5 4.5 0 0 0 7 0zm0 6.3a1.8 1.8 0 1 1 0-3.6 1.8 1.8 0 0 1 0 3.6z"/></svg>
        <span>Your Communication Address in<br>just two line</span>
      </li>
      <li>
        <svg viewBox="0 0 14 14"><path d="M1 4c0-2 2-3 6-3s6 1 6 3v1H10V4H4v1H1zM3 6h8l2 7H1z"/></svg>
        <span>(000) 000-000-000</span>
      </li>
      <li>
        <svg viewBox="0 0 14 14"><path d="M0 3h14v8H0zm1 1 6 4 6-4"/><path d="M1 4l6 4 6-4" fill="none" stroke="#f7f8f9" stroke-width="1"/></svg>
        <span>yourname@yourwebsite.com</span>
      </li>
      <li>
        <svg viewBox="0 0 14 14"><circle cx="7" cy="7" r="6.5"/><path d="M0.5 7h13M7 0.5v13M2 3.5h10M2 10.5h10" stroke="#f7f8f9" stroke-width="0.8" fill="none"/></svg>
        <span>www.yourwebsite.com</span>
      </li>
    </ul>
  </section>

  <section class="card card-front" aria-label="Card front">
    <div class="brand"><span class="brand-dot"></span><span class="brand-name">Kelnara</span></div>
    <div class="band"><span class="band-dark"></span><span class="band-light"></span></div>
  </section>

</main>
</body>
</html>
```